Harbor Key Realty - New Agent Opportunity Overview

We want to create a one (1) page brochure to highlight what Harbor Key Realty (a real estate brokerage) offers new agents. I have uploaded a Word doc that has all the text we want on the flyer. We want a professional looking design.
Industry/Entity Type
Real Estate Agent
Colors
3176b5
33a6d7

```html
<!DOCTYPE html>
<html lang="en">
<head>
<meta charset="utf-8">
<title>Harbor Key Realty – New Agent Opportunity</title>
<link href="https://fonts.googleapis.com/css2?family=Montserrat:wght@400;500;600;700;800&family=Source+Sans+3:wght@400;600;700&display=swap" rel="stylesheet">
<style>
:root{
  --brand-blue:#3176b5;
  --deep-blue:#20689f;
  --mid-blue:#2677ad;
  --sky-blue:#33a6d7;
  --pale-blue:#d6eaf5;
  --ink:#3a3a3a;
  --navy:#1c2b3a;
  --rule:#c9c9c9;
  --white:#ffffff;
}
*{margin:0;padding:0;box-sizing:border-box}
html,body{width:849px;height:1200px;overflow:hidden;background:var(--white)}
.flyer{position:relative;width:849px;height:1200px;overflow:hidden;font-family:"Source Sans 3",sans-serif;color:var(--ink)}
.hero-art{position:absolute;left:0;top:0}
.abs{position:absolute}
.wordmark{display:flex;align-items:center;gap:10px;font-family:"Montserrat",sans-serif;font-weight:700;white-space:nowrap;line-height:1}
.wordmark .mark{display:block;background:currentColor}
.brand-top{left:55px;top:42px;color:var(--white);font-size:20px;letter-spacing:2px}
.brand-top .mark{width:16px;height:16px}
.opening{right:55px;top:32px;text-align:right;color:var(--white);font-family:"Montserrat",sans-serif;font-weight:600;font-size:16.5px;line-height:21px}
.opening b{font-weight:700}
.headline{left:55px;top:474px;font-family:"Montserrat",sans-serif;color:var(--brand-blue);font-weight:800;font-size:38px;line-height:46px}
.headline .join{display:block;font-weight:700;font-size:23.5px;line-height:28px;margin-top:-2px}
.rule{left:55px;width:739px;height:1px;background:var(--rule)}
.rule.strong{height:2px;background:var(--brand-blue)}
.section-title{left:55px;font-family:"Source Sans 3",sans-serif;font-weight:700;font-size:15.5px;letter-spacing:.3px;color:var(--ink)}
.list{list-style:none;font-size:13.5px;line-height:17.2px}
.list li{position:relative;padding-left:27px}
.list li::before{content:"";position:absolute;left:0;top:4px;width:10px;height:10px;border:1.6px solid var(--sky-blue);border-radius:50%}
.list li.cont::before{display:none}
.split-label{font-size:14px;font-weight:600;color:var(--ink)}
.split-value{font-family:"Montserrat",sans-serif;color:var(--brand-blue);font-weight:600;font-size:57px;line-height:1;letter-spacing:-1px}
.split-value small{font-size:25px;letter-spacing:0}
.split-divider{width:1px;height:64px;background:var(--rule)}
.footer-band{left:0;top:1100px;width:849px;height:100px;background:linear-gradient(90deg,#2f7fbf,var(--sky-blue) 60%,#3a8fcb)}
.call{left:55px;top:1112px;color:var(--white);font-family:"Montserrat",sans-serif}
.call .lead{font-size:22px;font-weight:400;line-height:26px}
.call .phone{font-size:38px;font-weight:800;line-height:46px;letter-spacing:-.5px}
.brand-foot{right:55px;top:1122px;color:var(--navy);font-size:15px;letter-spacing:1.5px;gap:8px}
.brand-foot .mark{width:11px;height:11px}
.contact{right:55px;top:1152px;text-align:right;color:var(--white);font-size:15px;line-height:18px;letter-spacing:.2px}
</style>
</head>
<body>
<main class="flyer">
  <svg class="hero-art" width="849" height="600" viewBox="0 0 849 600">
    <defs>
      <linearGradient id="homeTones" x1="0" y1="0" x2="1" y2="1">
        <stop offset="0" stop-color="#f1c59a"/>
        <stop offset=".45" stop-color="#c97c5c"/>
        <stop offset="1" stop-color="#4c3a4c"/>
      </linearGradient>
      <linearGradient id="meetingTones" x1="0" y1="0" x2="1" y2="1">
        <stop offset="0" stop-color="#e3e4e6"/>
        <stop offset=".5" stop-color="#c9c3bb"/>
        <stop offset="1" stop-color="#8f7c66"/>
      </linearGradient>
    </defs>
    <polygon fill="var(--deep-blue)" points="0,0 849,0 849,314 560,476 345,269 220,198 131,248 42,199 42,94 0,71"/>
    <polygon fill="var(--mid-blue)" points="42,94 131,45 220,94 220,199 131,248 42,199"/>
    <polygon fill="var(--sky-blue)" points="246,136 286,114 326,136 326,184 286,207 246,184"/>
    <polygon fill="var(--sky-blue)" points="68,368 93,382 93,411 68,425 42,411 42,382"/>
    <polygon fill="url(#meetingTones)" role="img" aria-label="Photo: handshake over a desk with contract and small model house" points="220,225 327,283 327,408 220,471 112,408 112,283"/>
    <polygon fill="url(#homeTones)" role="img" aria-label="Photo: modern two-storey home at sunset" points="559,60 774,180 774,418 559,543 344,418 344,180"/>
    <polygon fill="var(--pale-blue)" points="326,437 366,460 366,506 326,529 286,506 286,460"/>
  </svg>

  <div class="abs wordmark brand-top"><span class="mark"></span>HARBOR KEY REALTY</div>
  <p class="abs opening">HKR Home Center Gaithersburg,<br><b>Maryland is Now Open!</b></p>

  <h1 class="abs headline">IGNITE YOUR<br>REAL ESTATE BUSINESS<span class="join">JOIN HARBOR KEY REALTY</span></h1>

  <div class="abs rule strong" style="top:605px"></div>
  <h2 class="abs section-title" style="top:620px">CONSUMER DIRECT ADVANTAGE</h2>
  <ul class="abs list" style="left:55px;top:656px">
    <li>Lender Referrals</li><li>Listwell Lead</li><li>Shared Lender Leads</li>
  </ul>
  <ul class="abs list" style="left:307px;top:657px">
    <li>Nestfinder.com /</li><li class="cont">OpenDoorsNearby.com</li><li>Credit Trigger Campaigns</li>
  </ul>
  <ul class="abs list" style="left:559px;top:657px">
    <li>Consumer Behavior Campaigns</li><li>HKR Call Center Marketing Team</li><li>HKR Sponsored Local Events</li>
  </ul>

  <div class="abs rule" style="top:721px"></div>
  <h2 class="abs section-title" style="top:733px">MAXIMIZED COMPENSATION</h2>
  <ul class="abs list" style="left:55px;top:769px">
    <li>No desk fees. No royalty fees. No franchise fees.</li><li>Company paid E&amp;O</li>
  </ul>
  <ul class="abs list" style="left:434px;top:770px">
    <li>Transaction fee of $550 includes Transaction Coordinator</li>
  </ul>

  <div class="abs rule" style="top:816px;width:716px"></div>
  <h2 class="abs section-title" style="top:831px">TYPE OF DEAL/COMMISSION SPLIT</h2>
  <div class="abs split-label" style="left:55px;top:862px">Self-Generated</div>
  <div class="abs split-value" style="left:55px;top:885px">90%<small>/ 10%</small></div>
  <div class="abs split-divider" style="left:298px;top:868px"></div>
  <div class="abs split-label" style="left:306px;top:862px">Lender Referred Leads</div>
  <div class="abs split-value" style="left:306px;top:885px">70%<small>/ 30%</small></div>
  <div class="abs split-divider" style="left:551px;top:868px"></div>
  <div class="abs split-label" style="left:559px;top:862px">HKR Generated Leads / Referrals</div>
  <div class="abs split-value" style="left:559px;top:885px">55%<small>/45%</small></div>

  <div class="abs rule" style="top:950px"></div>
  <h2 class="abs section-title" style="top:962px">COMPLETE SUPPORT SYSTEM</h2>
  <ul class="abs list" style="left:55px;top:998px">
    <li>Powerful Suite of Cloud Based Tools</li><li>IDX, CRM and Transaction Management</li><li>HKR Call Center Support for Leads and Deals</li><li class="cont">Transaction Coordinator</li><li class="cont">Virtual Assistants Available</li>
  </ul>
  <ul class="abs list" style="left:433px;top:997px">
    <li>24/7 Workspace Access</li><li>Coaching / Mentoring</li><li>Social Media / Marketing Expertise</li><li class="cont">Nationwide Partnerships with Top Lenders</li>
  </ul>

  <div class="abs footer-band"></div>
  <div class="abs call"><div class="lead">Call Us Now!</div><div class="phone">866-555-0142</div></div>
  <div class="abs wordmark brand-foot"><span class="mark"></span>HARBOR KEY REALTY</div>
  <p class="abs contact">support@harborkeyrealty.com<br>www.harborkeyrealty.com</p>
</main>
</body>
</html>
```